Business Card Re-Design/Update

We'd like to update out business cards. I've included our current "Style guide" which has the colour scheme of the organisation in it. I've also included the branding files with logos etc in them.

I've also included a copy of one of our existing cards so that you can see how ugly/dated they look. I'd like a fresh modern corporate look.

Target Market(s)

These are for our clients, potential clients, industry contacts - like all business cards

Contact Information for Business Card

Name
Position
Company Address - Level 1, 47 Garnet Lane, Toowong Qld 4066
Direct Phone
mobile
Email
Website -www.korvalnet.com.au
Logo

Colors

Designer to choose colors to be used in the design.

Requirements
Must have
• Main Logo
• Cards will need to be editable to be able to personalize them for each new employee.
Nice to have
• The MapOUT, HandOVER, UpKEEP would be okay to have if they can be sensibly and professionally added to the look without detracting from the main imagery.
• Maybe they could go on the back of the card? will leave this to your creative discretion as to whether/where they fit.
Should not have
• Should not have decorative or script fonts

```html
<!DOCTYPE html>
<html lang="en">
<head>
<meta charset="utf-8">
<title>korvalnet business card</title>
<link href="https://fonts.googleapis.com/css2?family=Lato:wght@400;700;900&display=swap" rel="stylesheet">
<style>
  :root {
    --red: #e3262b;
    --red-soft: #ee4a5a;
    --ink: #2e3338;
    --paper: #ffffff;
    --mist: #e8edf6;
    --stage: #dfe5e4;
    --green: #6cc04a;
    --purple: #9b3fd1;
    --blue: #3a8fe0;
  }
  * { margin: 0; padding: 0; box-sizing: border-box; }
  html, body { width: 1200px; height: 1200px; overflow: hidden; }
  body {
    background: var(--stage);
    font-family: "Lato", sans-serif;
    color: var(--ink);
    position: relative;
  }
  .card {
    position: absolute;
    left: 150px;
    width: 900px;
    height: 514px;
    border-radius: 34px;
    overflow: hidden;
    background: var(--paper);
    box-shadow: 0 10px 30px rgba(0,0,0,.12);
  }
  .card-back { top: 50px; background: var(--mist); }
  .card-front { top: 620px; }
  .card svg.graphics { position: absolute; inset: 0; }
  .back-band {
    position: absolute; left: 0; right: 0; top: 120px; height: 274px;
    background: #f4f7fc;
  }
  .wordmark {
    position: absolute; display: flex; align-items: center; gap: 16px;
    font-weight: 700; color: var(--ink); letter-spacing: .5px;
  }
  .wordmark .mark { background: var(--red); display: block; }
  .back-wordmark { left: 0; right: 0; top: 170px; justify-content: center; font-size: 54px; }
  .back-wordmark .mark { width: 40px; height: 40px; }
  .services {
    position: absolute; left: 0; right: 0; top: 252px;
    display: flex; justify-content: center; gap: 34px;
    font-size: 17px; font-weight: 700;
  }
  .services span::before {
    content: ""; display: inline-block; width: 10px; height: 10px;
    margin-right: 6px; background: currentColor; vertical-align: 1px;
  }
  .svc-map { color: var(--green); }
  .svc-keep { color: var(--purple); }
  .svc-hand { color: var(--blue); }
  .website {
    position: absolute; left: 0; right: 0; top: 345px;
    text-align: center; font-size: 24px; color: var(--ink);
  }
  .website em { font-style: normal; color: var(--red); }
  .front-wordmark { left: 240px; top: 75px; font-size: 78px; }
  .front-wordmark .mark { width: 56px; height: 56px; }
  .address {
    position: absolute; left: 230px; width: 520px; top: 236px;
    text-align: center; color: #fff; font-size: 20px; font-weight: 700; letter-spacing: .3px;
  }
  .person {
    position: absolute; right: 520px; top: 345px; text-align: right; white-space: nowrap;
  }
  .person .name { font-size: 36px; color: var(--ink); }
  .person .name b { font-weight: 900; }
  .person .role { font-size: 22px; color: var(--red); margin-top: 4px; }
  .divider {
    position: absolute; left: 410px; top: 340px; width: 3px; height: 100px; background: var(--red);
  }
  .contacts {
    position: absolute; left: 438px; top: 340px; font-size: 17px; line-height: 33px; white-space: nowrap;
  }
  .contacts b { font-weight: 900; display: inline-block; width: 20px; }
  .contacts .sep { color: var(--ink); margin: 0 12px; }
</style>
</head>
<body>

  <section class="card card-back" aria-label="Card back">
    <div class="back-band"></div>
    <svg class="graphics" width="900" height="514" viewBox="0 0 900 514">
      <polygon points="250,108 640,108 620,128 230,128" fill="#e3262b"/>
      <polygon points="290,300 700,300 680,318 310,318" fill="#e3262b"/>
    </svg>
    <div class="wordmark back-wordmark"><span class="mark"></span>korvalnet</div>
    <div class="services">
      <span class="svc-map">MapOUT</span>
      <span class="svc-keep">UpKEEP</span>
      <span class="svc-hand">HandOVER</span>
    </div>
    <p class="website">www.<em>korvalnet</em>.com.au</p>
  </section>

  <section class="card card-front" aria-label="Card front">
    <svg class="graphics" width="900" height="514" viewBox="0 0 900 514">
      <rect x="0" y="268" width="900" height="4" fill="#e3262b"/>
      <polygon points="200,226 780,226 750,276 230,276" fill="#e3262b"/>
    </svg>
    <div class="wordmark front-wordmark"><span class="mark"></span>korvalnet</div>
    <p class="address">Level 1, 47 Garnet Lane, Toowong Qld 4066</p>
    <div class="person">
      <p class="name"><b>Mara</b> Ellison</p>
      <p class="role">Business Development Manager</p>
    </div>
    <div class="divider"></div>
    <div class="contacts">
      <p><b>M</b>+61 (0)412 305 468<span class="sep">|</span><b>D</b>+61 (0)7 3870 4127</p>
      <p><b>P</b>+61 (0)7 3870 4120<span class="sep">|</span><b>F</b>+61 (0)7 3870 4199</p>
      <p><b>E</b>mellison@korvalnet.com.au</p>
    </div>
  </section>

</body>
</html>
```